High End Personalized Functional Medicine in Women's Health

We are adding new and exciting personalized medicine services to our Women's Health Care practice focusing on health optimization and anti-aging as well as hormone replacement therapy and need a high end brochure to educate patients about these services. We would like to see a zen-like design that has feminine appeal. Our office colors are vibrant but soothing. We have utilized the concepts of feng shui to optimize our positive energy. The exterior of the building is peach and cream and these colors would blend with that energy The final design should communicate a sense that you can take control of your health and aging.
Updates

Target Market(s)

Females age 35-65 with annual income >$75000/year

Industry/Entity Type

Health And Wellness

Logo Text

Bright Path is the company name. Our sister company is Mesa Rio Ob/Gyn

Font styles to use
Serif

Colors

Designer to choose colors to be used in the design.

Requirements
Must have
• My project must have clean lines. I like a strong feminine appearance, not a fluffy curvy feminine look. Professional appearance, Brochure would be on thicker card stock. A strong front page that makes you want to open the brochure
Nice to have
• Eye catching photos that complement our message . I am not tied to the peach and cream color recommendation, but find those colors feminine but not so cliche as pinks and purples.
Should not have
• frilly design

```html
<!DOCTYPE html>
<html lang="en">
<head>
<meta charset="utf-8">
<title>Bright Path Functional Medicine – Brochure</title>
<link href="https://fonts.googleapis.com/css2?family=EB+Garamond:ital,wght@0,400;0,600;1,400;1,600&display=swap" rel="stylesheet">
<style>
  :root {
    --green: #2a8a3a;
    --gold: #dca21c;
    --cream: #f7f4df;
    --cream-light: #fbf9ec;
    --ink: #1f1f1f;
    --backdrop: #d4d5d7;
  }
  * { box-sizing: border-box; margin: 0; padding: 0; }
  html, body { width: 1200px; height: 800px; overflow: hidden; }
  body { background: var(--backdrop); font-family: "EB Garamond", Georgia, serif; color: var(--ink); }

  .brochure {
    position: absolute; left: 30px; top: 30px; width: 1140px; height: 740px;
    display: flex; box-shadow: 0 8px 24px rgba(0,0,0,.18);
  }
  .panel { position: relative; width: 380px; height: 740px; background: var(--cream); overflow: hidden; }
  .panel + .panel { border-left: 1px solid rgba(0,0,0,.08); }
  .band { position: absolute; left: 0; width: 380px; display: block; }
  .band--top { top: 0; }
  .band--bottom { bottom: 0; }

  .photo { position: absolute; }

  /* Inside left panel */
  .question {
    position: absolute; left: 30px; width: 320px;
    color: var(--green); font-style: italic; font-weight: 600; font-size: 17px;
    line-height: 1.1; text-align: center; text-decoration: underline;
  }
  .body-copy {
    position: absolute; font-size: 12.5px; line-height: 1.3;
    font-style: italic; text-align: justify;
  }

  /* Middle panel */
  .bio-title {
    position: absolute; top: 50px; left: 0; width: 380px; text-align: center;
    color: var(--green); font-size: 27px; font-weight: 400;
  }
  .bio-copy {
    position: absolute; left: 22px; top: 438px; width: 336px;
    font-size: 14px; line-height: 1.32; text-align: justify;
  }

  /* Cover */
  .cover-title {
    position: absolute; top: 52px; left: 0; width: 380px; text-align: center;
    color: var(--gold); font-weight: 600; font-size: 38px; line-height: 1.1;
  }
  .cover-quote {
    position: absolute; left: 26px; top: 612px; width: 328px;
    font-size: 17px; line-height: 1.3; text-align: justify;
  }
</style>
</head>
<body>
<div class="brochure">

  <!-- Inside panel: questions -->
  <section class="panel panel--questions">
    <svg class="band band--top" height="40" viewBox="0 0 380 40" preserveAspectRatio="none">
      <path d="M0 0H380V40C250 18 120 14 0 30Z" fill="var(--green)"/>
      <path d="M0 0H70C50 8 25 16 0 22Z" fill="var(--gold)"/>
    </svg>
    <h2 class="question" style="top:52px">Why should<br>you consider a functional medicine visit?</h2>
    <p class="body-copy" style="left:30px;top:100px;width:320px">You are tired of feeling tired. You can’t even focus on the future because you are so overwhelmed. The pain of being unable to think clearly and being too tired to exercise are your daily reality. Your life goals seem like too much to think about, you just have to get through today.</p>
    <div class="photo" role="img" aria-label="Smiling women stretching in a bright fitness class" style="left:0;top:198px;width:380px;height:150px;background:linear-gradient(120deg,#c9d6e4,#e9d3c4 45%,#f4efe6 70%,#8fb6dc)"></div>
    <h2 class="question" style="top:358px">Who else should<br>consider a functional medicine visit?</h2>
    <p class="body-copy" style="left:30px;top:404px;width:320px">You want to achieve OPTIMAL health with a personalized medicine approach. You are eating well, exercising and engaging in stress reducing activities such as meditation. You want to know how to minimize the effects of aging and are ready to take a proactive approach in getting to the highest level of health you can achieve.</p>
    <div class="photo" role="img" aria-label="Three generations of a smiling family posing together" style="left:0;top:484px;width:380px;height:200px;background:linear-gradient(110deg,#e8d7bf,#b8a18a 40%,#d9c6b2 70%,#eef0f2)"></div>
    <svg class="band band--bottom" height="64" viewBox="0 0 380 64" preserveAspectRatio="none">
      <path d="M0 8C120 30 260 40 380 30V64H0Z" fill="var(--green)"/>
    </svg>
  </section>

  <!-- Inside panel: doctor biography -->
  <section class="panel panel--bio">
    <svg class="band band--top" height="50" viewBox="0 0 380 50" preserveAspectRatio="none">
      <path d="M0 0H380V18C250 40 120 44 0 40Z" fill="var(--green)"/>
    </svg>
    <h1 class="bio-title">Dr. Navarro with family</h1>
    <div class="photo" role="img" aria-label="Doctor and her family sitting together on ivy-covered grass outdoors" style="left:22px;top:100px;width:336px;height:325px;background:linear-gradient(180deg,#8a7358 0%,#6e6a45 40%,#3f5a2a 75%,#2e4420)"></div>
    <p class="bio-copy">Dr. Elena Navarro specializes in women’s health and has over 25 years of experience. She is an expert in bio-identical hormone replacement therapy and has been a Subderma bio-identical hormone pellet practitioner for over 10 years. Dr. Navarro has been practicing functional medicine for many years with a primary focus on hormone therapy, medical weight loss, and lifestyle change. She has recently expanded her practice to incorporate additional services including healing with a focus on adrenal, gastrointestinal and detoxification programs. Dr. Navarro is a practitioner of the Hart Method for functional medicine and works closely with Dr. Samuel Hart as her mentor in the development of individual treatment protocols for our patients. Dr. Hart has over 25 years of experience in functional medicine.</p>
    <svg class="band band--bottom" height="70" viewBox="0 0 380 70" preserveAspectRatio="none">
      <path d="M0 30C130 48 260 46 380 32V70H0Z" fill="var(--green)"/>
      <path d="M0 50C130 62 260 60 380 48V70H0Z" fill="var(--gold)"/>
    </svg>
  </section>

  <!-- Front cover -->
  <section class="panel panel--cover">
    <svg class="band band--top" height="50" viewBox="0 0 380 50" preserveAspectRatio="none">
      <path d="M0 0H380V36C250 16 120 10 0 18Z" fill="var(--gold)"/>
    </svg>
    <h1 class="cover-title">Bright Path<br>Functional Medicine</h1>
    <div class="photo" role="img" aria-label="Smiling physician in a white coat with stethoscope greeting an older patient" style="left:0;top:180px;width:380px;height:400px;background:linear-gradient(120deg,#e9eef1 0%,#c9d4dc 35%,#f5f5f3 60%,#4f7db0 75%,#eceff1)"></div>
    <svg class="band" style="top:548px" height="70" viewBox="0 0 380 70" preserveAspectRatio="none">
      <path d="M0 20C40 0 90 0 140 18C220 40 300 36 380 28V70H0Z" fill="var(--green)"/>
      <path d="M0 40C130 60 260 56 380 44V70H0Z" fill="var(--gold)"/>
      <path d="M0 54C130 72 260 68 380 58V70H0Z" fill="var(--cream)"/>
    </svg>
    <p class="cover-quote">Functional medicine’s aim is to heal the physical body in order to engage in our life purpose of connection and emotional and spiritual growth.</p>
    <svg class="band band--bottom" height="44" viewBox="0 0 380 44" preserveAspectRatio="none">
      <path d="M0 10C130 30 260 30 380 16V44H0Z" fill="var(--gold)"/>
    </svg>
  </section>

</div>
</body>
</html>
```